Hello Creative Minds!
Our business is after a elegant and classy flyer that draws attention!
The business is Velmora Turf - Lawn Rejuvenation Services. We provide services that maintain a healthy and vibrant green lawn through the tough Australian seasons. The products we use limits the water needed to keep grass green to a minimum - practically none at all! This not only helps the home owner or home seller but the environment by limiting the use of water that is needed to create a green lawn. The products we use are made from natural ingredients that are and pet friendly.
This fly will be our introductory offer to the market. Below are the required points that need to be on the flyer. Attached is the business logo, before & after pictures and 1 example of the LAYOUT not DESIGN of what the flyer should be laid out like or similar to. Feel free to use different 'Lawn Mower' pictures.
All the best; if you need any questions answered please feel free to message.
REQUIRED POINTS (Please re-phrase were possible);
*Instantly restores the natural green colour of grass – year round
*Lasts for up to 3 months
*Substantially reduces watering needs
*Pet friendly
*Stays green during droughts and water restrictions
*UV fade resistant
*Won’t bleed, run, or stain once absorbed into the grass
*Safe for the environment, pets and people
*Works in extreme heat, cold and frost
*Organic and natural – no harmful chemicals
*Reduces the amount of fertilizer
and water used on lawns
*Kerb appeal is essential for getting your property sold for the highest price possible
SERVICES & PRICING
Lawn maintenance (cut & trim) starting from $60
Lawn rejuvenation starting from $80 (Only $27 a month for 3 months)*
Package deal starting from $120
Introductory offer: 25% off all services. Refer a friend, when they book you receive another 25% off your next service.
LOCATIONS
Nowra to Sydney
CONTACT NUMBER
Will be posted with the winner - please leave an area for this.
SOCIAL MEDIA
Please add Chatterloop and Snapvista logo's
Updates
Competition has finished, thank you to all that have participated! I will review and comment on the flyers that need assistance. All the best with future designs!
Target Market(s)
home owners, home sellers, property developers, real estates and nursing homes and government housing.
Industry/Entity Type
Lawn Care
Look and feel
Each slider illustrates characteristics of the customer's brand and the style your logo design should communicate.

```html
<!DOCTYPE html>
<html lang="en">
<head>
<meta charset="utf-8">
<title>Velmora Turf - Lawn Rejuvenation Services</title>
<link href="https://fonts.googleapis.com/css2?family=Montserrat:wght@400;700;800;900&family=Zilla+Slab:wght@500&display=swap" rel="stylesheet">
<style>
  :root {
    --page-bg: #e8e5e0;
    --paper: #ffffff;
    --green: #1b8a3a;
    --green-dark: #14702d;
    --green-text: #16863a;
    --yellow: #d6cc2a;
    --yellow-band: #ccc72a;
    --red: #d7182a;
    --red-dark: #9c0f1c;
    --ink: #0d0d0d;
    --white: #ffffff;
    --heading: "Montserrat", sans-serif;
    --body: "Zilla Slab", serif;
  }
  * { margin: 0; padding: 0; box-sizing: border-box; }
  html, body { width: 1200px; height: 800px; overflow: hidden; }
  body { background: var(--page-bg); position: relative; font-family: var(--heading); }

  .flyer {
    position: absolute; left: 324px; top: 10px;
    width: 551px; height: 780px;
    background: var(--paper); overflow: hidden;
    box-shadow: 0 2px 10px rgba(0,0,0,.15);
  }
  .corner-accent { position: absolute; left: 0; top: 0; }

  .hero {
    position: absolute; left: 21px; top: 21px; width: 508px; height: 263px;
    border-radius: 10px; overflow: hidden;
    background: linear-gradient(160deg, #2f5d1f 0%, #3f8a2a 35%, #27a040 60%, #4f9b2b 100%);
  }
  .hero-photo { position: absolute; inset: 0; }
  .brand-name {
    position: absolute; left: 0; right: 0; top: 170px; text-align: center;
    font-family: var(--heading); font-weight: 800; font-size: 44px; color: var(--white);
    letter-spacing: 1px;
  }
  .brand-tagline {
    position: absolute; left: 0; right: 0; top: 242px; text-align: center;
    font-family: var(--heading); font-weight: 400; font-size: 12.5px; color: var(--white);
    letter-spacing: 6px;
  }

  .benefit-rail {
    position: absolute; left: 23px; top: 286px; width: 27px; height: 212px;
    background: var(--green); border-radius: 2px;
  }
  .benefits { position: absolute; left: 24px; top: 291px; list-style: none; }
  .benefits li {
    height: 17.2px; display: flex; align-items: center;
    font-family: var(--body); font-weight: 500; font-size: 13.3px; color: var(--green-text);
    white-space: nowrap;
  }
  .benefits svg { width: 25px; margin-right: 6px; flex: none; }

  .offer-badge {
    position: absolute; left: 375px; top: 312px; width: 154px; height: 154px; border-radius: 50%;
    background: radial-gradient(circle at 40% 30%, #e8202f 0%, var(--red) 45%, var(--red-dark) 100%);
    box-shadow: 3px 4px 6px rgba(0,0,0,.25);
    color: var(--white); text-align: center; font-family: var(--heading);
  }
  .offer-kicker { margin-top: 13px; font-weight: 800; font-size: 14px; line-height: 14px; }
  .offer-amount { font-weight: 900; font-size: 27px; line-height: 28px; margin-top: 1px; }
  .offer-scope { font-weight: 900; font-size: 21.5px; line-height: 24px; }
  .offer-referral { font-weight: 700; font-size: 8.4px; line-height: 9.4px; margin-top: 5px; padding: 0 6px; }

  .price { position: absolute; font-family: var(--heading); text-align: center; }
  .price-label {
    position: absolute; background: var(--yellow); color: var(--ink);
    font-weight: 800; font-size: 15px; line-height: 20px; white-space: nowrap;
  }
  .price-label small { font-size: 10px; font-weight: 800; }
  .price-value {
    position: absolute; background: var(--green); color: var(--white);
    font-weight: 800; font-size: 19.5px; line-height: 23px; white-space: nowrap;
  }
  .price-value small { display: block; font-size: 9.5px; line-height: 8px; font-weight: 700; }
  .package-deal {
    position: absolute; left: 0; width: 378px; top: 607px; text-align: center;
    font-weight: 800; font-size: 17.5px; color: var(--green-text);
  }

  .grass-band {
    position: absolute; left: 0; width: 551px; background: linear-gradient(180deg, #2c8f33, #1f7a2a);
  }
  .locations {
    position: absolute; left: 25px; top: 640px; color: var(--white);
    font-family: var(--heading); font-weight: 900; line-height: 23px;
  }
  .locations .title { font-size: 23px; letter-spacing: 1px; }
  .locations .area { font-size: 26px; letter-spacing: 1px; }

  .results {
    position: absolute; left: 355px; top: 504px; width: 172px; height: 171px;
    background: var(--white); padding: 1.5px; box-shadow: 2px 2px 4px rgba(0,0,0,.3);
  }
  .result {
    position: relative; height: 84px; margin-bottom: 1.5px;
  }
  .result.before { background: linear-gradient(180deg, #6d706c 0%, #6d706c 30%, #a7a55a 45%, #6e6f70 75%, #c9c3b3 100%); }
  .result.after { background: linear-gradient(180deg, #6d706c 0%, #6d706c 35%, #5aa23a 50%, #6e6f70 75%, #c9c3b3 100%); }
  .result-tag {
    position: absolute; right: 5px; top: 14px; font-family: var(--heading); font-weight: 900; font-size: 12px;
  }
  .before .result-tag { color: var(--red); }
  .after .result-tag { color: #21b24a; top: 16px; }

  .contact-band {
    position: absolute; left: 0; top: 692px; width: 551px; height: 75px; background: var(--yellow-band);
  }
  .phone {
    position: absolute; left: 27px; top: 16px;
    font-family: var(--heading); font-weight: 900; font-size: 35px; color: var(--ink); letter-spacing: -1px;
  }
  .socials { position: absolute; left: 406px; top: 8px; list-style: none; }
  .socials li {
    display: flex; align-items: center; height: 18px;
    font-family: var(--heading); font-weight: 800; font-size: 12px; color: var(--ink);
  }
  .socials .dot { width: 11px; height: 11px; background: var(--green); margin-right: 6px; }
</style>
</head>
<body>
<main class="flyer">
  <svg class="corner-accent" width="190" height="170" viewBox="0 0 190 170" aria-hidden="true">
    <polygon points="0,0 186,0 0,166" fill="#1b8a3a"/>
  </svg>

  <section class="hero">
    <div class="hero-photo" role="img" aria-label="Photo of a green petrol lawn mower on a freshly cut lawn in a sunny garden"></div>
    <h1 class="brand-name">Velmora Turf</h1>
    <p class="brand-tagline">LAWN REJUVENATION SERVICES</p>
  </section>

  <div class="benefit-rail"></div>
  <ul class="benefits">
    <li><svg viewBox="0 0 25 14" aria-hidden="true"><path d="M9 7l3 3 5-6" fill="none" stroke="#fff" stroke-width="2"/></svg>Instantly restores the natural green colour of grass – year round</li>
    <li><svg viewBox="0 0 25 14" aria-hidden="true"><path d="M9 7l3 3 5-6" fill="none" stroke="#fff" stroke-width="2"/></svg>Lasts for up to 3 months</li>
    <li><svg viewBox="0 0 25 14" aria-hidden="true"><path d="M9 7l3 3 5-6" fill="none" stroke="#fff" stroke-width="2"/></svg>Substantially reduces watering needs</li>
    <li><svg viewBox="0 0 25 14" aria-hidden="true"><path d="M9 7l3 3 5-6" fill="none" stroke="#fff" stroke-width="2"/></svg>Pet friendly</li>
    <li><svg viewBox="0 0 25 14" aria-hidden="true"><path d="M9 7l3 3 5-6" fill="none" stroke="#fff" stroke-width="2"/></svg>Stays green during droughts and water restrictions</li>
    <li><svg viewBox="0 0 25 14" aria-hidden="true"><path d="M9 7l3 3 5-6" fill="none" stroke="#fff" stroke-width="2"/></svg>UV fade resistant</li>
    <li><svg viewBox="0 0 25 14" aria-hidden="true"><path d="M9 7l3 3 5-6" fill="none" stroke="#fff" stroke-width="2"/></svg>Won’t bleed, run, or stain once absorbed into the grass</li>
    <li><svg viewBox="0 0 25 14" aria-hidden="true"><path d="M9 7l3 3 5-6" fill="none" stroke="#fff" stroke-width="2"/></svg>Safe for the environment, pets and people</li>
    <li><svg viewBox="0 0 25 14" aria-hidden="true"><path d="M9 7l3 3 5-6" fill="none" stroke="#fff" stroke-width="2"/></svg>Works in extreme heat, cold and frost</li>
    <li><svg viewBox="0 0 25 14" aria-hidden="true"><path d="M9 7l3 3 5-6" fill="none" stroke="#fff" stroke-width="2"/></svg>Organic and natural – no harmful chemicals</li>
    <li><svg viewBox="0 0 25 14" aria-hidden="true"><path d="M9 7l3 3 5-6" fill="none" stroke="#fff" stroke-width="2"/></svg>Reduces the amount of fertilizer and water used on lawns</li>
    <li><svg viewBox="0 0 25 14" aria-hidden="true"><path d="M9 7l3 3 5-6" fill="none" stroke="#fff" stroke-width="2"/></svg>Kerb appeal is essential for getting your property sold for the highest price possible</li>
  </ul>

  <aside class="offer-badge">
    <p class="offer-kicker">SPECIAL<br>OFFER</p>
    <p class="offer-amount">25% OFF</p>
    <p class="offer-scope">all services.</p>
    <p class="offer-referral">Refer a friend, when they book you receive another 25% off your next service.</p>
  </aside>

  <div class="price-label" style="left:79px;top:504px;width:221px;text-align:center;">Lawn maintenance <small>(cut &amp; trim)</small></div>
  <div class="price-value" style="left:77px;top:524px;width:225px;height:23px;text-align:center;">starting from $60</div>
  <div class="price-label" style="left:104px;top:553px;width:170px;text-align:center;">Lawn rejuvenation</div>
  <div class="price-value" style="left:77px;top:571px;width:225px;height:29px;text-align:center;">starting from $80<small>(Only $27 a month for 3 months)*</small></div>
  <p class="package-deal">Package deal starting from $120</p>

  <div class="grass-band" style="top:636px;height:56px;" role="img" aria-label="Close-up texture of green lawn grass"></div>
  <div class="locations">
    <p class="title">LOCATIONS</p>
    <p class="area">NOWRA TO SYDNEY</p>
  </div>

  <figure class="results">
    <div class="result before" role="img" aria-label="Backyard lawn looking dry and patchy before treatment"><span class="result-tag">BEFORE</span></div>
    <div class="result after" role="img" aria-label="The same backyard lawn looking lush and green after treatment"><span class="result-tag">AFTER</span></div>
  </figure>

  <footer class="contact-band">
    <p class="phone">Ph: 987-654-321</p>
    <ul class="socials">
      <li><span class="dot"></span>Snapvista</li>
      <li><span class="dot"></span>Chatterloop</li>
    </ul>
  </footer>
  <div class="grass-band" style="top:767px;height:13px;" role="img" aria-label="Strip of green lawn grass"></div>
</main>
</body>
</html>
```